依頼詳細
ポスティング形式での営業となりますので、
一目見て目に付くようなチラシデザインで
あれば、多少デザインに派手さが入っても
良いとは思っています。

「本当に和室のままでイイですか?」
というアラートの様なタイトルがどれだけ
目を引くかに重点を置いて考えています。

また、何故和室を洋室に変えた方がイイと
いう根拠につきましては、
・畳の経年寿命の早さとメンテナンス&交換をしてない畳のアレルギー等の促進を
進めるという情報をわかりやすくアラートをお伝えした文章が欲しいです。(ハウスダスト・ダニ・花粉)

価格帯の記載
・マンションアパートタイプであれば
1畳単価50000円〜
・戸建てタイプの場合い1畳単価60000円〜
押し入れのクローゼット化 10000円〜

室内の物の移動等も含める作業は別途
お見積もりとの別記載も入れて欲しい。

和室〜洋室に変えた際のビフォーアフターの
写真等も添付したいです。
記載項目
翠昇株式会社 03-6812-3097
HP https://suishoweb.ne.jp/
キャッチコピー「和室のままで本当にイイですか?」
サイズ
A4
ページ数
両面
希望イメージ
シンプル 複雑
単色 カラフル
暗い 明るい
日常 高級
遊び心 厳粛
未来的 伝統的
女性的 男性的
希望する色
青系
納品ファイル
• 高解像度JPG (.jpg)
• PNG形式 (.png)
補足説明
デザイン 文章 画像についても提案があれば都度頂きたい。
■ 選んだ理由

シンプルで有りながらも、ディテールの部分の丁寧さがスゴく見やすく思えました。文章につきましても
拙い説明にも関わらず、しっかり拾い上げて頂けたのが1番決め手となりました。本当にありがとうございます。

■ 提案者全員のお礼・コメント

この度は沢山のご提案頂きありがとうございました。
タスクフォルンを使ったのは初めてで、色々分からず皆様に失礼が有りましたらここでお詫びさせて下さい。

とてもタスクフォルンのサービスとデザイナーの皆様の
技術に大変関心を持ちました。今後も色んな事で
運用したいと思っておりますので、また機会が
ございましたら何卒よろしくお願い致します。

この度は誠に有難うございました。

```html
<!DOCTYPE html>
<html lang="ja">
<head>
<meta charset="utf-8">
<title>和室のままで本当にイイですか？</title>
<link href="https://fonts.googleapis.com/css2?family=Noto+Sans+JP:wght@400;500;700;900&display=swap" rel="stylesheet">
<style>
:root{
  --tatami-light:#c9b27c;
  --tatami-mid:#b39a62;
  --tatami-dark:#8f7a48;
  --blue:#1f5fae;
  --blue-deep:#184c90;
  --navy:#1b3f7a;
  --yellow:#ffe33a;
  --sun:#f4c21a;
  --gray-box:#e6eaef;
  --gray-text:#4a5260;
  --gray-icon:#9aa3ae;
  --blue-box:#e3eefb;
  --white:#ffffff;
  --ink:#1a1a1a;
}
*{margin:0;padding:0;box-sizing:border-box}
html,body{width:849px;height:1200px;overflow:hidden;background:var(--white)}
body{font-family:"Noto Sans JP",sans-serif;color:var(--ink)}
.flyer{position:relative;width:849px;height:1200px;overflow:hidden;background:var(--white)}

.hero-photo{position:absolute;left:0;top:0;width:849px;height:600px;
  background:linear-gradient(100deg,var(--tatami-light) 0%,var(--tatami-mid) 55%,var(--tatami-dark) 100%)}

.quote-marks{position:absolute;top:22px;left:0;width:100%;text-align:center;
  font-size:64px;font-weight:900;color:var(--white);letter-spacing:40px;line-height:1;
  text-shadow:0 0 3px rgba(0,0,0,.6),2px 3px 6px rgba(0,0,0,.45)}

.title-kanji{position:absolute;left:0;width:100%;text-align:center;
  font-weight:900;color:var(--white);line-height:1;font-size:200px;
  -webkit-text-stroke:4px #2a2a2a;paint-order:stroke fill;
  text-shadow:4px 6px 10px rgba(0,0,0,.45)}
.title-kanji.wa{top:80px}
.title-kanji.shitsu{top:285px}

.title-kana{position:absolute;top:478px;left:0;width:100%;text-align:center;
  font-size:68px;font-weight:900;color:var(--white);line-height:1;
  -webkit-text-stroke:3px #2a2a2a;paint-order:stroke fill;
  text-shadow:3px 4px 8px rgba(0,0,0,.4)}

.alert-band{position:absolute;left:0;top:580px;width:849px;height:285px;background:var(--blue)}
.alert-question{position:absolute;top:608px;left:0;width:100%;text-align:center;
  font-size:78px;font-weight:900;color:var(--white);line-height:1.1;letter-spacing:1px}
.sub-strip{position:absolute;top:752px;left:170px;width:510px;height:34px;background:var(--yellow);
  font-size:20px;font-weight:700;color:var(--ink);text-align:center;line-height:34px}
.proposal{position:absolute;top:805px;left:0;width:100%;text-align:center;
  font-size:23px;font-weight:700;color:var(--white)}

.merits-title{position:absolute;top:890px;left:0;width:100%;text-align:center;
  font-size:42px;font-weight:900;color:var(--navy);line-height:1.1}
.merits-title .raku{color:var(--sun);font-size:48px}

.col-label{position:absolute;top:958px;font-size:16px;font-weight:500;color:var(--gray-text)}
.col-label.left{left:172px}
.col-label.right{left:590px}

.compare{position:absolute;top:988px;left:28px;width:793px}
.row{display:flex;align-items:center;height:44px;margin-bottom:10px}
.box{display:flex;align-items:center;height:44px;padding:0 12px;gap:12px;font-size:16px;font-weight:700}
.box.before{width:372px;background:var(--gray-box);color:var(--gray-text)}
.box.after{width:381px;background:var(--blue-box);color:var(--blue-deep)}
.dot{flex:none;width:28px;height:28px;border-radius:50%}
.before .dot{background:var(--gray-icon)}
.after .dot{background:var(--sun)}
.arrow{flex:none;width:40px;height:44px;display:flex;align-items:center;justify-content:center}
</style>
</head>
<body>
<main class="flyer">
  <div class="hero-photo" role="img" aria-label="畳の和室の床の写真（縦に走る緑の畳縁）"></div>
  <div class="quote-marks">＼／</div>
  <div class="title-kanji wa">和</div>
  <div class="title-kanji shitsu">室</div>
  <div class="title-kana">のままで</div>

  <div class="alert-band"></div>
  <h1 class="alert-question">本当にイイですか？</h1>
  <p class="sub-strip">永く住まう場所だから、快適に暮らせる空間に</p>
  <p class="proposal">翠昇は、“和室から洋室へのリフォーム”をご提案いたします。</p>

  <h2 class="merits-title">洋室にすれば「<span class="raku">楽</span>」がたくさん</h2>
  <span class="col-label left">和室（畳）</span>
  <span class="col-label right">洋室（フローリング）</span>

  <section class="compare">
    <div class="row">
      <div class="box before"><span class="dot"></span>定期的なメンテナンス・交換が必要</div>
      <div class="arrow"><svg width="16" height="22" viewBox="0 0 16 22"><path d="M3 2 L13 11 L3 20" fill="none" stroke="#1f5fae" stroke-width="3"/></svg></div>
      <div class="box after"><span class="dot"></span>基本的にメンテナンスが必要ないから「楽」</div>
    </div>
    <div class="row">
      <div class="box before"><span class="dot"></span>カビ・ダニ対策の掃除やお手入れが大変</div>
      <div class="arrow"><svg width="16" height="22" viewBox="0 0 16 22"><path d="M3 2 L13 11 L3 20" fill="none" stroke="#1f5fae" stroke-width="3"/></svg></div>
      <div class="box after"><span class="dot"></span>普段の掃除やお手入れが「楽」</div>
    </div>
    <div class="row">
      <div class="box before"><span class="dot"></span>立ち座りに足腰の負担がかかる</div>
      <div class="arrow"><svg width="16" height="22" viewBox="0 0 16 22"><path d="M3 2 L13 11 L3 20" fill="none" stroke="#1f5fae" stroke-width="3"/></svg></div>
      <div class="box after"><span class="dot"></span>椅子やベッドを置けば立ち座りが「楽」</div>
    </div>
    <div class="row">
      <div class="box before"><span class="dot"></span>重量物を置くと畳がへこんでしまう</div>
      <div class="arrow"><svg width="16" height="22" viewBox="0 0 16 22"><path d="M3 2 L13 11 L3 20" fill="none" stroke="#1f5fae" stroke-width="3"/></svg></div>
      <div class="box after"><span class="dot"></span>家具などの配置も自在だから「楽しい」</div>
    </div>
  </section>
</main>
</body>
</html>
```